Website Redesign - Gleam Packs (2 - Pages)

We want a new website that is improved from our first website. Here is an example of a better website: http://www.grinvelora.com/
See our logo attached for design start.
Page 1:
We want a website that looks as good as this but want the following features:
- Top Bar with following Text: Whitening Kits, Whitening Pens, Pulse Aura, Gleam Bristle, Accessories & Refills, Instructions, Contact Us
- Right Justified @ top My Account, Checkout
- Static top page image with our ultimate kit photo (attached: Gleam Packs - Ultimate Kit.jpg) and an "Order Now" yellow button on the page (See www.tarnolvex.com for example)
- Five Categories (Teeth Whitening Kits, Teeth Whitening Pens, Pulse Aura, Gleam Bristle, Accessories & Refills) all accompanied with pictures and a text bar with name at bottom of pictures... Pulse Aura is a sonic facial brush (don't currently have picture, a filler picture is fine). Gleam Bristle is an electronic tooth brush (again don't have product photo)
- Three Pictures Side by Side Pictures to explain product "Save Money", "Whiten Like a Dentist", "Fast Results" (See www.brenquorel.com under why bren quorel with three photos)...
- Reviews ("I love this product!!!", "Works great. Took only 3 sessions to a great smile", "It worked exactly as I had hoped and was simple to use")
- Bottom Order Now Bar (Again, see www.brenquorel.com bottom of page)
Page 2:
Take the instructions and make them part of a cohesive easy to follow page. See Instructions 1, 2, 3

```html
<!DOCTYPE html>
<html lang="en">
<head>
<meta charset="utf-8">
<title>Gleam Packs — Teeth Whitening</title>
<link rel="stylesheet" href="https://fonts.googleapis.com/css2?family=Open+Sans:wght@400;600;700&family=Arimo:wght@400;700&display=swap">
<style>
:root{
  --blue:#1566a9;
  --blue-dark:#0f5592;
  --blue-light:#2a8fd8;
  --ink:#1a6aa8;
  --topbar:#2b2b2b;
  --footer:#1f1f1f;
  --paper:#f6f6f6;
  --card:#f3f3f3;
  --grey-text:#777;
  --orange:#e89a1c;
  --orange-dark:#c97d0c;
  --white:#ffffff;
}
*{box-sizing:border-box;margin:0;padding:0}
html,body{width:821px;height:1200px;overflow:hidden;background:var(--paper)}
body{font-family:"Open Sans",Arial,sans-serif;color:#333}
.page{position:relative;width:821px;height:1200px;overflow:hidden;background:var(--paper)}
.abs{position:absolute}

/* top utility bar */
.utility-bar{left:0;top:0;width:821px;height:18px;background:var(--topbar)}
.utility-links{position:absolute;right:115px;top:3px;display:flex;gap:12px;font-size:7.5px;letter-spacing:.6px;color:#ddd;text-transform:uppercase}
.utility-links span{display:flex;align-items:center;gap:4px}

/* header */
.site-header{left:0;top:18px;width:821px;height:57px;background:var(--blue)}
.brand{position:absolute;left:121px;top:20px;font-size:10.5px;font-weight:600;color:var(--white);letter-spacing:.3px;text-transform:uppercase;white-space:nowrap}
.main-nav{position:absolute;left:206px;top:21px;width:500px;display:flex;justify-content:space-between;font-size:7.3px;letter-spacing:.4px;color:var(--white);text-transform:uppercase;white-space:nowrap;border-bottom:1px solid rgba(255,255,255,.25);padding-bottom:6px}
.header-pointer{left:230px;top:74px;width:0;height:0;border-left:7px solid transparent;border-right:7px solid transparent;border-top:11px solid var(--blue)}

/* product band */
.product-band{left:0;top:350px;width:821px;height:254px;background:linear-gradient(180deg,var(--blue) 0%,#1a6fb2 100%)}

/* hero */
.hero-frame{left:117px;top:94px;width:593px;height:293px;background:linear-gradient(180deg,#e3e6ee,#c9cfdb);box-shadow:0 8px 16px rgba(0,0,0,.25)}
.hero-stage{left:128px;top:106px;width:570px;height:268px;overflow:hidden;background:linear-gradient(135deg,#f2f3f7,#d7dae3)}
.hero-photo{left:45px;top:38px;width:330px;height:215px;border-radius:6px;background:radial-gradient(ellipse at 45% 50%,rgba(90,140,210,.35),rgba(255,255,255,0) 70%)}
.hero-title{left:372px;top:67px;width:180px;text-align:center;font-size:20px;line-height:21px;font-weight:400;letter-spacing:1.2px;color:var(--white);text-transform:uppercase;white-space:nowrap}
.hero-title .sub{color:#e3f1ff}
.hero-rule{left:390px;width:144px;height:1px;background:rgba(255,255,255,.4)}
.btn-order{display:flex;align-items:center;justify-content:center;background:linear-gradient(180deg,#f3ad2c,var(--orange-dark));color:var(--white);font-size:13px;letter-spacing:1.2px;text-transform:uppercase;border-radius:2px;box-shadow:0 1px 2px rgba(0,0,0,.3);white-space:nowrap}
.hero-btn{left:388px;top:133px;width:152px;height:28px}

/* category row */
.section-rule-title{left:128px;top:408px;width:580px;display:flex;align-items:center;gap:14px;color:var(--white);font-size:15px;letter-spacing:1.5px;text-transform:uppercase;white-space:nowrap}
.section-rule-title::before,.section-rule-title::after{content:"";flex:1;height:4px;border-top:1px solid rgba(255,255,255,.4);border-bottom:1px solid rgba(255,255,255,.4)}
.category{width:110px;text-align:center}
.category-thumb{width:102px;height:102px;margin:0 auto;border-radius:50%;background:var(--white);border:5px solid var(--blue-light);box-shadow:0 0 0 2px rgba(255,255,255,.25)}
.category-thumb div{width:100%;height:100%;border-radius:50%;background:radial-gradient(circle at 50% 50%,#bfe0f2 0%,#e8f3fa 45%,#ffffff 70%)}
.category-label{margin-top:7px;font-size:7px;font-weight:600;letter-spacing:.5px;color:var(--white);text-transform:uppercase;white-space:nowrap}

/* why choose */
.why-title{left:0;top:622px;width:821px;text-align:center;font-size:17px;font-weight:400;letter-spacing:1.3px;color:var(--ink);text-transform:uppercase}
.feature-disc{width:127px;height:127px;border-radius:50%;background:var(--blue);display:flex;align-items:center;justify-content:center}
.divider{top:685px;width:1px;height:223px;background:#d4d4d4}
.divider-notch{width:8px;height:14px;background:var(--paper);border:1px solid #d4d4d4;border-left:none;border-bottom:none;transform:rotate(45deg)}
.feature-card{width:141px;height:95px;background:var(--card);box-shadow:0 3px 2px -1px #cfcfcf;padding:8px 9px}
.feature-card h3{text-align:center;font-family:Arimo,Arial,sans-serif;font-size:10px;font-weight:700;letter-spacing:.6px;color:var(--ink);text-transform:uppercase;margin-bottom:9px;white-space:nowrap}
.feature-card p{font-family:Arimo,Arial,sans-serif;font-size:8px;line-height:11px;color:var(--grey-text);text-align:justify}

/* testimonials */
.reviews-band{left:0;top:930px;width:821px;height:144px;background:linear-gradient(180deg,#ececec,#dcdcdc)}
.quote-mark{font-family:Georgia,serif;font-size:110px;line-height:1;color:rgba(0,0,0,.06)}
.review{width:196px;height:82px;background:var(--white);border-radius:2px;box-shadow:0 2px 3px rgba(0,0,0,.18);padding:10px 8px;display:flex;gap:6px}
.review-photo{flex:none;width:58px;height:50px;border:1px solid #ccc;background:linear-gradient(180deg,#9fcbe6 0%,#cfe3ef 45%,#6a4b3c 46%,#e7d6c8 100%)}
.review-text{font-family:Arimo,Arial,sans-serif;font-size:8px;line-height:10.5px;color:#555}
.review-author{margin-top:5px;font-weight:700;color:var(--ink)}

/* call to action */
.cta-band{left:0;top:1074px;width:821px;height:102px;background:linear-gradient(180deg,var(--blue),var(--blue-dark))}
.cta-text{left:162px;top:1111px;display:flex;align-items:center;gap:10px;font-size:20px;letter-spacing:2px;color:var(--white);text-transform:uppercase;white-space:nowrap}
.cta-brand{font-size:14px;font-weight:600;letter-spacing:.6px;padding:3px 8px;background:rgba(255,255,255,.08)}
.cta-btn{left:501px;top:1109px;width:152px;height:29px}

/* footer */
.site-footer{left:0;top:1176px;width:821px;height:24px;background:var(--footer);font-family:Arimo,Arial,sans-serif;font-size:8px;color:#ddd;padding:6px 0 0 121px;letter-spacing:.3px}
</style>
</head>
<body>
<div class="page">

  <div class="abs utility-bar">
    <div class="utility-links">
      <span><svg width="7" height="7" viewBox="0 0 10 10"><circle cx="5" cy="3" r="2.4" fill="#ddd"/><path d="M0.5 10c0-3 2-4.5 4.5-4.5S9.5 7 9.5 10z" fill="#ddd"/></svg>My Account</span>
      <span><svg width="9" height="7" viewBox="0 0 12 10"><path d="M0 1h2l1.5 6h7L12 2.5H3" fill="none" stroke="#ddd" stroke-width="1.2"/><circle cx="4.5" cy="9" r="1" fill="#ddd"/><circle cx="9.5" cy="9" r="1" fill="#ddd"/></svg>Checkout</span>
    </div>
  </div>

  <header class="abs site-header">
    <div class="brand">Gleam Packs</div>
    <nav class="main-nav">
      <span>Whitening Kits</span><span>Whitening Pens</span><span>Pulse Aura</span><span>Gleam Bristle</span><span>Accessories &amp; Refills</span><span>Instructions</span><span>Contact</span>
    </nav>
  </header>
  <div class="abs header-pointer"></div>

  <div class="abs product-band"></div>

  <div class="abs hero-frame"></div>
  <div class="abs hero-stage">
    <svg class="abs" style="left:0;top:0" width="570" height="268" viewBox="0 0 570 268">
      <polygon points="0,0 130,0 0,190" fill="#1a6fb4"/>
      <polygon points="475,0 570,0 570,268 345,268" fill="#1b73b8"/>
    </svg>
    <div class="abs hero-photo" role="img" aria-label="Ultimate whitening kit: LED mouthpiece light, shade guide, gel syringe, trays, swab and bottle"></div>
    <div class="abs hero-rule" style="top:59px"></div>
    <div class="abs hero-title">Gleam Packs<br><span class="sub">Ultimate Kit</span></div>
    <div class="abs hero-rule" style="top:119px"></div>
    <div class="abs btn-order hero-btn">Order Now</div>
  </div>

  <div class="abs section-rule-title">Gleam Packs</div>

  <div class="abs category" style="left:122px;top:449px"><div class="category-thumb"><div role="img" aria-label="Teeth whitening kit in open case"></div></div><div class="category-label">Teeth Whitening Kits</div></div>
  <div class="abs category" style="left:243px;top:449px"><div class="category-thumb"><div role="img" aria-label="Teeth whitening pens"></div></div><div class="category-label">Teeth Whitening Pens</div></div>
  <div class="abs category" style="left:364px;top:449px"><div class="category-thumb"><div role="img" aria-label="Sonic facial brush"></div></div><div class="category-label">Pulse Aura</div></div>
  <div class="abs category" style="left:485px;top:449px"><div class="category-thumb"><div role="img" aria-label="Electronic toothbrush"></div></div><div class="category-label">Gleam Bristle</div></div>
  <div class="abs category" style="left:605px;top:449px"><div class="category-thumb"><div role="img" aria-label="Accessories and refills"></div></div><div class="category-label">Accessories &amp; Refills</div></div>

  <h2 class="abs why-title">Why Choose Gleam Packs</h2>

  <div class="abs divider" style="left:320px"></div>
  <div class="abs divider-notch" style="left:316px;top:776px"></div>
  <div class="abs divider" style="left:537px"></div>
  <div class="abs divider-notch" style="left:533px;top:776px"></div>

  <div class="abs feature-disc" style="left:155px;top:677px" role="img" aria-label="Piggy bank symbol for saving money"></div>
  <div class="abs feature-disc" style="left:364px;top:677px" role="img" aria-label="Cheerful tooth character giving a thumbs up"></div>
  <div class="abs feature-disc" style="left:571px;top:677px">
    <svg width="66" height="66" viewBox="0 0 66 66">
      <circle cx="33" cy="33" r="29" fill="none" stroke="#fff" stroke-width="4"/>
      <g fill="#fff"><rect x="31.5" y="8" width="3" height="5"/><rect x="31.5" y="53" width="3" height="5"/><rect x="8" y="31.5" width="5" height="3"/><rect x="53" y="31.5" width="5" height="3"/></g>
      <path d="M33 33V16M33 33l12 8" stroke="#fff" stroke-width="3.5" stroke-linecap="round" fill="none"/>
    </svg>
  </div>

  <div class="abs feature-card" style="left:153px;top:813px"><h3>Save Money</h3><p>Lorem ipsum dolor sit amet, consectetur adipiscing elit. Suspendisse sed pulvinar purus. Nullam non congue augue</p></div>
  <div class="abs feature-card" style="left:357px;top:813px"><h3>Whiten Like a Dentist</h3><p>Lorem ipsum dolor sit amet, consectetur adipiscing elit. Suspendisse sed pulvinar purus. Nullam non congue augue</p></div>
  <div class="abs feature-card" style="left:571px;top:813px"><h3>Fast Results</h3><p>Lorem ipsum dolor sit amet, consectetur adipiscing elit. Suspendisse sed pulvinar purus. Nullam non congue augue</p></div>

  <div class="abs reviews-band"></div>
  <div class="abs quote-mark" style="left:60px;top:925px">&ldquo;</div>
  <div class="abs quote-mark" style="left:720px;top:978px">&rdquo;</div>

  <div class="abs review" style="left:114px;top:965px"><div class="review-photo" role="img" aria-label="Customer portrait"></div><div class="review-text">I love this product, It really works great and you can see fast results!<div class="review-author">-Mara Linwood</div></div></div>
  <div class="abs review" style="left:327px;top:965px"><div class="review-photo" role="img" aria-label="Customer portrait"></div><div class="review-text">I love this product, It really works great and you can see fast results!<div class="review-author">-Mara Linwood</div></div></div>
  <div class="abs review" style="left:545px;top:965px"><div class="review-photo" role="img" aria-label="Customer portrait"></div><div class="review-text">I love this product, It really works great and you can see fast results!<div class="review-author">-Mara Linwood</div></div></div>

  <div class="abs cta-band"></div>
  <div class="abs cta-text">Get Your <span class="cta-brand">Gleam Packs</span> Today!</div>
  <div class="abs btn-order cta-btn">Order Now</div>

  <footer class="abs site-footer">Copyright 2014 Gleam Packs. &nbsp;Terms &amp; Conditions &nbsp;| &nbsp;Privacy Policy</footer>

</div>
</body>
</html>
```